Platelet Rich Plasma (PRP) Flyer

Hi,

Looking to spruce up our Platelet Rich Plasma Flyer (see power point attachment). I also included previous flyers as examples on the design style we are looking for.

Quorum is our official font of our logo.
Attached is our logo in EPS format.
Please use the current photos in the power point. If you include photos, please make sure the stock image is free.

Files must be under 5MB. JPEG, PNG, PDF, .ai

Thank you,
Dorian

Target Market(s)

Patients

Industry/Entity Type

Healthcare

Font styles to use
Other font styles liked:
• Quorum

Requirements
Must have
• Emphasis on Platelet Rich Plasma Therapy when they pick up the flyer. The price of $199. FSA/HSA Eligible. The different treatment areas. The three addresses. Best of the best logo can be very small, not as important.
Nice to have
• One or two pictures. Less is more
Should not have
• Long paragraphs, multiple sentences.

```html
<!DOCTYPE html>
<html lang="en">
<head>
<meta charset="utf-8">
<title>Platelet Rich Plasma Therapy Flyer</title>
<link rel="stylesheet" href="https://fonts.googleapis.com/css2?family=Allura&family=Archivo:wght@700;800&family=Poppins:wght@400;500;600;700&display=swap">
<style>
:root{
  --page:#f4f4f4;
  --dark:#2a2a2a;
  --dark-soft:#3a3a3a;
  --teal:#54c3a7;
  --teal-text:#3fc4a1;
  --teal-deep:#2d7c5e;
  --orange:#f07a43;
  --ink:#2b2b2b;
  --white:#ffffff;
}
*{box-sizing:border-box;margin:0;padding:0}
html,body{width:1200px;height:2401px;overflow:hidden;background:var(--page)}
body{position:relative;font-family:"Poppins",sans-serif}
.flyer{
  position:absolute;left:40px;top:475px;width:992px;height:1283px;
  transform:scale(1.13);transform-origin:top left;overflow:hidden;
  background:radial-gradient(ellipse at 50% 30%,var(--dark-soft) 0%,var(--dark) 70%);
  box-shadow:0 14px 40px rgba(0,0,0,.25);
}
.abs{position:absolute}
.brand{left:0;right:0;top:62px;display:flex;justify-content:center;align-items:center;gap:12px}
.brand-dot{width:26px;height:26px;border-radius:50%;background:var(--teal)}
.brand-name{font-family:"Archivo",sans-serif;font-weight:800;font-size:30px;color:var(--orange);letter-spacing:.5px}
.script{left:0;right:0;top:140px;text-align:center;font-family:"Allura",cursive;font-size:118px;color:var(--teal-text);line-height:1}
.headline{left:0;right:0;top:228px;text-align:center;font-family:"Archivo",sans-serif;font-weight:800;font-size:70px;color:var(--orange);letter-spacing:1px}
.dots{left:0;right:0;top:307px;display:flex;justify-content:center;gap:6px}
.dots span{width:7px;height:7px;background:var(--white)}
.intro{left:60px;right:60px;top:330px;text-align:center;color:var(--white);font-size:17px;line-height:22px}
.intro .lead{color:var(--teal-text);font-weight:600;font-size:18px}
.eligible{left:0;right:0;top:392px;display:flex;justify-content:center}
.eligible span{border:2px solid var(--teal-text);border-radius:24px;color:var(--teal-text);font-family:"Archivo",sans-serif;font-weight:800;font-size:22px;letter-spacing:3px;padding:4px 26px}
.bg-shapes{left:0;top:0}
.treating{left:300px;top:474px;width:390px;height:66px;background:var(--orange);border-radius:6px;color:var(--white);font-family:"Archivo",sans-serif;font-weight:800;font-size:52px;letter-spacing:12px;text-align:center;line-height:66px;box-shadow:0 4px 8px rgba(0,0,0,.25)}
.condition{width:220px;text-align:center;color:var(--ink);font-weight:500;font-size:21px;line-height:26px;top:657px}
.icon-ring{width:64px;height:64px;border-radius:50%;background:var(--white);border:4px solid var(--orange);display:flex;align-items:center;justify-content:center}
.photo{top:740px;width:282px;height:175px;border-radius:12px;border:2px solid var(--white)}
.photo.knee{left:64px;background:linear-gradient(135deg,#1c3550,#2d4b6a 60%,#8a4a3a)}
.photo.lab{left:355px;background:linear-gradient(135deg,#2d4f86,#d8d5d0 55%,#f2efe9)}
.photo.heel{left:647px;background:linear-gradient(135deg,#1f1f1f,#4a3a34 45%,#e0b49e)}
.price-label{left:55px;top:948px;width:293px;height:55px;background:var(--dark);border-radius:8px 0 0 8px;color:var(--white);font-size:30px;font-weight:500;line-height:55px;padding-left:18px}
.price-value{left:350px;top:948px;width:440px;height:55px;background:var(--orange);color:var(--white);font-family:"Archivo",sans-serif;font-weight:800;font-size:31px;line-height:55px;padding-left:28px}
.price-value .cur{font-size:16px;position:relative;top:-12px;margin-right:2px}
.shield{left:772px;top:878px}
.shield-text{left:772px;top:920px;width:160px;text-align:center;color:var(--white);font-size:14px;line-height:18px}
.shield-text b{font-weight:700}
.shield-text .big{font-family:"Archivo",sans-serif;font-weight:800;font-size:42px;line-height:52px}
.feature{top:1028px;display:flex;align-items:center;gap:14px;color:var(--ink);font-size:20px;font-weight:500;line-height:24px}
.feature .icon-ring{width:60px;height:60px}
.office{top:1122px;width:195px;height:103px;background:var(--dark);color:var(--white);text-align:center;font-size:12.5px;line-height:15px;padding-top:24px}
.office h3{color:var(--teal-text);font-size:16px;font-weight:600;margin-bottom:4px}
.pin{top:1112px;width:22px;height:22px}
.contact-title{left:676px;top:1126px;color:var(--white);font-family:"Archivo",sans-serif;font-weight:700;font-size:20px;letter-spacing:4px}
.phone{left:672px;top:1152px;display:flex;align-items:center;gap:8px;color:var(--white);font-size:30px;font-weight:600}
.web{left:668px;top:1193px;width:324px;height:36px;background:var(--orange);color:var(--white);font-size:21px;line-height:36px;padding-left:22px}
.web b{font-weight:700}
</style>
</head>
<body>
<main class="flyer">
  <svg class="abs bg-shapes" width="992" height="1283" viewBox="0 0 992 1283">
    <path d="M0 735 C150 545 330 478 496 478 C662 478 842 545 992 735 L992 1283 L0 1283 Z" fill="var(--teal-deep)"/>
    <path d="M0 760 C160 575 335 498 496 498 C657 498 832 575 992 760 L992 1283 L0 1283 Z" fill="var(--teal)"/>
    <g stroke="var(--white)" stroke-width="2" fill="none">
      <path d="M370 540 V552 H278 V575"/>
      <path d="M482 540 V575"/>
      <path d="M615 540 V552 H706 V575"/>
    </g>
  </svg>

  <header class="abs brand">
    <span class="brand-dot"></span>
    <span class="brand-name">RIDGEVIEW FOOT &amp; ANKLE</span>
  </header>

  <div class="abs script">Platelet Rich</div>
  <h1 class="abs headline">PLASMA THERAPY (PRP)</h1>
  <div class="abs dots"><span></span><span></span><span></span><span></span><span></span><span></span><span></span><span></span></div>

  <section class="abs intro">
    <p class="lead">PRP uses your own blood to help damaged tissue heal.</p>
    <p>A consultation is required to make sure you qualify.</p>
  </section>
  <div class="abs eligible"><span>FSA / HSA ELIGIBLE</span></div>

  <div class="abs treating">TREATING</div>

  <div class="abs icon-ring" style="left:246px;top:575px">
    <svg width="28" height="34" viewBox="0 0 28 34"><path d="M14 2 C22 2 24 10 21 18 C19 24 20 32 14 32 C8 32 9 24 7 18 C4 10 6 2 14 2Z" fill="var(--orange)"/></svg>
  </div>
  <div class="abs icon-ring" style="left:450px;top:575px">
    <svg width="26" height="34" viewBox="0 0 26 34"><path d="M6 2 H14 V22 L22 26 V32 H6 Z" fill="var(--orange)"/><path d="M18 8 l4 -2 M18 13 l4 0 M18 18 l4 2" stroke="var(--orange)" stroke-width="2"/></svg>
  </div>
  <div class="abs icon-ring" style="left:681px;top:575px">
    <svg width="34" height="30" viewBox="0 0 34 30"><path d="M4 2 H14 V16 L30 20 V28 H4 Z" fill="var(--orange)"/><path d="M8 6 H12 M8 10 H12" stroke="var(--white)" stroke-width="2"/></svg>
  </div>

  <div class="abs condition" style="left:170px">Plantar<br>Fasciitis</div>
  <div class="abs condition" style="left:372px">Tendon &amp;<br>Ligament Injuries</div>
  <div class="abs condition" style="left:600px">Achilles<br>Tendonitis</div>

  <div class="abs photo knee" role="img" aria-label="Photo of a person holding a painful knee"></div>
  <div class="abs photo lab" role="img" aria-label="Photo of a gloved hand placing blood tubes in a centrifuge"></div>
  <div class="abs photo heel" role="img" aria-label="Photo of a hand touching a sore heel"></div>

  <div class="abs price-label">SELF PAY PRICE</div>
  <div class="abs price-value"><span class="cur">$</span>199 PER TREATMENT</div>

  <svg class="abs shield" width="160" height="200" viewBox="0 0 160 200">
    <defs><linearGradient id="shieldFill" x1="0" y1="0" x2="0" y2="1"><stop offset="0" stop-color="#f0393f"/><stop offset="1" stop-color="#a8151b"/></linearGradient></defs>
    <path d="M80 4 C105 20 130 24 156 24 V100 C156 150 120 180 80 196 C40 180 4 150 4 100 V24 C30 24 55 20 80 4Z" fill="url(#shieldFill)" stroke="#fff" stroke-width="3"/>
  </svg>
  <div class="abs shield-text"><b>OUR DOCTORS</b><br>ARE ON CALL AT<br>THE CITY ER<div class="big">24/7</div></div>

  <div class="abs feature" style="left:55px">
    <div class="icon-ring"><svg width="26" height="26" viewBox="0 0 26 26"><rect x="2" y="5" width="22" height="19" rx="2" fill="var(--orange)"/><rect x="6" y="12" width="14" height="8" fill="var(--white)" opacity=".8"/><rect x="6" y="2" width="3" height="6" fill="var(--orange)"/><rect x="17" y="2" width="3" height="6" fill="var(--orange)"/></svg></div>
    <span>Same<br>Day</span>
  </div>
  <div class="abs feature" style="left:204px">
    <div class="icon-ring"><svg width="28" height="26" viewBox="0 0 28 26"><path d="M7 20 V13 A7 7 0 0 1 21 13 V20 Z" fill="var(--orange)"/><rect x="4" y="20" width="20" height="4" fill="var(--orange)"/><path d="M14 1 V4 M3 6 l2 2 M25 6 l-2 2" stroke="var(--orange)" stroke-width="2"/></svg></div>
    <span>Emergency</span>
  </div>
  <div class="abs feature" style="left:420px">
    <div class="icon-ring"><svg width="26" height="26" viewBox="0 0 26 26"><rect x="2" y="5" width="22" height="19" rx="2" fill="var(--orange)"/><path d="M13 11 V21 M8 16 H18" stroke="var(--white)" stroke-width="3"/><rect x="6" y="2" width="3" height="6" fill="var(--orange)"/><rect x="17" y="2" width="3" height="6" fill="var(--orange)"/></svg></div>
    <span>Saturday<br>Appointments</span>
  </div>

  <div class="abs office" style="left:55px"><h3>Northgate Office</h3>215 Maple Crest<br>Dr.Suite120 Northgate,<br>MD20000</div>
  <div class="abs office" style="left:257px"><h3>Riverside Office</h3>48 Wellness Way<br>Riverside,WV20000</div>
  <div class="abs office" style="left:458px"><h3>Lakeside Office</h3>900 Harbor View<br>Blvd.Suite 305 Lakeside,<br>MD20001</div>
  <svg class="abs pin" style="left:141px" viewBox="0 0 22 22"><circle cx="11" cy="11" r="10" fill="var(--orange)"/><path d="M11 5 a4 4 0 0 1 4 4 c0 3 -4 7 -4 7 s-4 -4 -4 -7 a4 4 0 0 1 4 -4z" fill="#fff"/></svg>
  <svg class="abs pin" style="left:343px" viewBox="0 0 22 22"><circle cx="11" cy="11" r="10" fill="var(--orange)"/><path d="M11 5 a4 4 0 0 1 4 4 c0 3 -4 7 -4 7 s-4 -4 -4 -7 a4 4 0 0 1 4 -4z" fill="#fff"/></svg>
  <svg class="abs pin" style="left:544px" viewBox="0 0 22 22"><circle cx="11" cy="11" r="10" fill="var(--orange)"/><path d="M11 5 a4 4 0 0 1 4 4 c0 3 -4 7 -4 7 s-4 -4 -4 -7 a4 4 0 0 1 4 -4z" fill="#fff"/></svg>

  <div class="abs contact-title">CONTACT US TODAY</div>
  <div class="abs phone">
    <svg width="32" height="32" viewBox="0 0 32 32"><circle cx="16" cy="16" r="15" fill="var(--white)"/><path d="M10 8 l4 0 l1 5 l-2 2 c1 3 3 5 6 6 l2 -2 l5 1 l0 4 c-10 1 -17 -6 -16 -16z" fill="var(--orange)"/></svg>
    <span>(555)014-2260</span>
  </div>
  <div class="abs web">www.<b>stepwellclinic</b>.com</div>
</main>
</body>
</html>
```